Crestwell Renewal Business Card Design Phase 2

Professional and clean design. The design colors should flow with the logo. Two-sided card with the website on the back which is:

www.CrestwellRenewal.example.

"Specializing in Water Damage Restoration"

On the front I need the name, email, phone, and logo.

Name: Dorian Halvek
Email: Dorian@CrestwellRenewal.example
Phone: 555-318-2046 for now

I only have the Preview and Thumbnail right now but should have the source files uploaded within a day or two.

Target Market(s)

Flood victims, home owners with water damage from busted pipes etc...

Industry/Entity Type

Business

Contact Information for Business Card

Name: Dorian Halvek

Font styles to use
Serif
Sans Serif

Requirements
Must have
• Business Card Details Info

```html
<!DOCTYPE html>
<html lang="en">
<head>
<meta charset="utf-8">
<title>Crestwell Renewal Business Card</title>
<link href="https://fonts.googleapis.com/css2?family=Source+Sans+3:wght@400;600;700&display=swap" rel="stylesheet">
<style>
  :root {
    --navy: #1f3864;
    --green: #3a8a2e;
    --divider: #cfe3c8;
    --ink: #1a1a1a;
    --card: #ffffff;
    --backdrop-top: #262626;
    --backdrop-bottom: #050505;
  }
  * { box-sizing: border-box; margin: 0; padding: 0; }
  html, body { width: 1200px; height: 900px; overflow: hidden; }
  body {
    position: relative;
    background: linear-gradient(180deg, var(--backdrop-top) 0%, #141414 55%, var(--backdrop-bottom) 100%);
    font-family: "Source Sans 3", "Myriad Pro", Arial, sans-serif;
  }
  .card {
    position: absolute;
    top: 306px;
    width: 440px;
    height: 271px;
    background: var(--card);
    border-radius: 12px;
    overflow: hidden;
  }
  .card--front { left: 149px; }
  .card--back { left: 608px; }

  /* Front */
  .front-brand {
    position: absolute;
    left: 22px;
    top: 104px;
    width: 150px;
    display: flex;
    align-items: center;
    gap: 8px;
    color: var(--navy);
    font-weight: 700;
    font-size: 19px;
    line-height: 1.05;
  }
  .front-brand__square {
    flex: 0 0 14px;
    height: 14px;
    background: var(--navy);
  }
  .front-divider {
    position: absolute;
    left: 189px;
    top: 72px;
    width: 1px;
    height: 140px;
    background: var(--divider);
  }
  .person-name {
    position: absolute;
    left: 201px;
    top: 85px;
    font-size: 17px;
    font-weight: 600;
    color: var(--navy);
  }
  .person-name__first { color: var(--green); }
  .contact-list {
    position: absolute;
    left: 202px;
    top: 138px;
    list-style: none;
  }
  .contact-list__item {
    display: flex;
    align-items: center;
    gap: 7px;
    font-size: 13px;
    color: var(--ink);
    height: 19px;
  }
  .contact-list__icon { width: 9px; height: 9px; fill: var(--green); }

  /* Back */
  .back-brand {
    position: absolute;
    left: 0;
    right: 0;
    top: 72px;
    text-align: center;
    color: var(--navy);
    font-weight: 700;
    font-size: 44px;
    line-height: 0.98;
    letter-spacing: 0.5px;
  }
  .website {
    position: absolute;
    left: 0;
    right: 0;
    top: 196px;
    text-align: center;
    color: var(--green);
    font-weight: 600;
    font-size: 13px;
  }
  .tagline-band {
    position: absolute;
    left: 17px;
    top: 240px;
    width: 406px;
    height: 25px;
    background: var(--navy);
    color: #fff;
    font-weight: 600;
    font-size: 15px;
    display: flex;
    align-items: center;
    justify-content: center;
  }
</style>
</head>
<body>
  <section class="card card--front">
    <div class="front-brand">
      <span class="front-brand__square"></span>
      <span>Crestwell Renewal</span>
    </div>
    <div class="front-divider"></div>
    <h1 class="person-name"><span class="person-name__first">Dorian</span> Halvek</h1>
    <ul class="contact-list">
      <li class="contact-list__item">
        <svg class="contact-list__icon" viewBox="0 0 10 10"><path d="M2 0.5 L3.6 2.6 L2.7 3.6 Q3.8 6 6.4 7.3 L7.4 6.4 L9.5 8 L8.3 9.5 Q4.5 9 1.8 5.8 Q0.3 3.6 0.6 1.6 Z"/></svg>
        <span>555-318-2046</span>
      </li>
      <li class="contact-list__item">
        <svg class="contact-list__icon" viewBox="0 0 10 10"><path d="M0 2 H10 V8.5 H0 Z M0.6 2.4 L5 5.6 L9.4 2.4" stroke="#fff" stroke-width="0.8"/></svg>
        <span>Dorian@CrestwellRenewal.example</span>
      </li>
    </ul>
  </section>

  <section class="card card--back">
    <div class="back-brand">Crestwell<br>Renewal</div>
    <p class="website">www.CrestwellRenewal.example</p>
    <div class="tagline-band">Specializing in Water Damage Restoration</div>
  </section>
</body>
</html>
```